RW Frameworks Inc Business cards

We need business cards using our existing logo but slightly modified. Right now the logo says RW Framework Masonry. We want to keep the RW part of the design, but replace the Framework Masonry portion with "FRAMEWORKS". Please see the attached file.
Ideally this would be a blank template so we can add Different Names, titles, and phone numbers later.
On the one side we want only the logo and on the other side the detail. I'm attaching an example for you to see.
Please reach out with any other questions. Our address and other details will be given out once we find a design we like.

Target Market(s)

Construction Industry

```html
<!DOCTYPE html>
<html lang="en">
<head>
<meta charset="utf-8">
<title>RW Frameworks Inc Business Cards</title>
<link href="https://fonts.googleapis.com/css2?family=Arimo:wght@400;700&display=swap" rel="stylesheet">
<style>
  :root {
    --stage: #e4e4e2;
    --card-white: #ffffff;
    --card-dark: #333335;
    --brand-blue: #1e74c6;
    --ink-grey: #6f7072;
    --emboss-grey: #5a5b5e;
    --edge-blue: #2a7fd0;
  }
  * { box-sizing: border-box; margin: 0; padding: 0; }
  html, body {
    width: 1200px; height: 900px; overflow: hidden;
    background: var(--stage);
    font-family: "Arimo", Arial, sans-serif;
  }
  .canvas { position: relative; width: 1200px; height: 900px; }
  .card {
    position: absolute; width: 560px; height: 320px;
    border-bottom: 4px solid var(--edge-blue);
    box-shadow: 0 6px 18px rgba(0,0,0,0.18);
  }
  .card--front { left: 60px; top: 90px; background: var(--card-white); }
  .card--back { left: 580px; top: 490px; background: var(--card-dark); }

  .wordmark { position: absolute; text-align: left; font-weight: 700; }
  .wordmark__initials { display: block; font-size: 92px; line-height: 1; letter-spacing: 2px; }
  .wordmark__name { display: block; font-size: 22px; letter-spacing: 9px; margin-top: 6px; }

  .card--front .wordmark { left: 48px; top: 102px; color: var(--brand-blue); }
  .card--back .wordmark {
    left: 50%; top: 50%; transform: translate(-50%, -50%);
    color: var(--emboss-grey); text-align: center;
  }
  .card--back .wordmark__initials { font-size: 110px; }
  .card--back .wordmark__name { font-size: 26px; letter-spacing: 11px; }

  .divider {
    position: absolute; left: 300px; top: 88px;
    width: 2px; height: 150px; background: var(--brand-blue);
  }
  .details { position: absolute; left: 322px; top: 84px; color: var(--ink-grey); font-size: 13px; line-height: 1.35; }
  .details__name { color: var(--brand-blue); font-weight: 700; font-size: 17px; line-height: 1.1; }
  .details__title { margin-bottom: 10px; }
  .details__address { margin-bottom: 8px; }
  .contact { display: flex; align-items: center; gap: 6px; }
  .contact svg { width: 11px; height: 11px; flex: none; fill: var(--brand-blue); }
</style>
</head>
<body>
<main class="canvas">
  <section class="card card--front" aria-label="Business card, detail side">
    <div class="wordmark">
      <span class="wordmark__initials">RW</span>
      <span class="wordmark__name">FRAMEWORKS</span>
    </div>
    <div class="divider"></div>
    <div class="details">
      <p class="details__name">DANIEL HARTE</p>
      <p class="details__title">President</p>
      <p class="details__address">48 Millbrook Yard<br>Cedar Falls NY 12840</p>
      <p class="contact">
        <svg viewBox="0 0 12 12" aria-hidden="true"><path d="M2.5 1l2 2-1.2 1.6c.7 1.5 1.8 2.6 3.3 3.3L8.2 6.7l2 2-1.3 2.1C5 10.5 1.5 7 1.2 2.2z"/></svg>
        555-014-2270
      </p>
      <p class="contact">
        <svg viewBox="0 0 12 12" aria-hidden="true"><path d="M3 0.5h6v11H3zM4 1.8v7.6h4V1.8z"/></svg>
        555-014-2281
      </p>
      <p class="contact">
        <svg viewBox="0 0 12 12" aria-hidden="true"><path d="M0.5 2.5h11v7h-11zM1.5 3.5L6 7l4.5-3.5z"/></svg>
        info@rwframeworks.example
      </p>
      <p class="contact">
        <svg viewBox="0 0 12 12" aria-hidden="true"><circle cx="6" cy="6" r="5.2"/></svg>
        www.rwframeworks.example
      </p>
    </div>
  </section>

  <section class="card card--back" aria-label="Business card, logo side">
    <div class="wordmark">
      <span class="wordmark__initials">RW</span>
      <span class="wordmark__name">FRAMEWORKS</span>
    </div>
  </section>
</main>
</body>
</html>
```